Class A Builder, Construction Company, Foundation repair

We need a design for our construction company. We want to highlight that we are a Class A Contractor and new Home construction & Additions on one side, and maybe on the back express or foundation repair and termite damager repair services. I have attached our current business card we are trying to improve on. Also I would like to use the color scheme from out website www.KTHouseMend.net (you are welcome to use pictures or art work found on there as well) Last if we can put the QTR Logo on there. Ofcourse we would like our contact information.

Dunlow Construction, Inc
4827 E. Halbrim Dr.
Norfolk, VA 23999
555-214-3907
DunlowConstruction@mailbrook.net
www.KTHouseMend.net

PS: We no longer need the Lorvix Services Logo from the old card.

Target Market(s)

Construction, Additions, Foundation Repair, Termite damage repair

Industry/Entity Type

Residential Construction

Contact Information for Business Card

Foundation Repair Specialist

Requirements
Must have
• Dunlow Construction, Inc
• 555-214-3907
• DunlowConstruction@mailbrook.net
• www.KTHouseMend.net
• Class A Builder
• QTR Logo
Nice to have
• 4827 E. Halbrim Dr.
• Norfolk, VA 23999
• Fax Number 555-214-8641
Should not have
• Lorvix Services Logo from old card.

```html
<!DOCTYPE html>
<html lang="en">
<head>
<meta charset="utf-8">
<title>Dunlow Construction – Business Card</title>
<link rel="stylesheet" href="https://fonts.googleapis.com/css2?family=Montserrat:wght@400;700;800;900&display=swap">
<style>
  :root {
    --page: #ffffff;
    --card-cream: #f2ebdd;
    --photo-light: #e6dcc8;
    --photo-mid: #d6c9ae;
    --photo-ground: #cfc3a0;
    --brand-dark: #0b0b0b;
    --brand-brown: #6b4a2c;
    --band-brown: #6a4a2d;
    --band-line: #3f2a17;
    --contact-brown: #6b5034;
  }
  html, body {
    margin: 0;
    width: 1200px;
    height: 1000px;
    overflow: hidden;
    background: var(--page);
    font-family: "Montserrat", sans-serif;
  }
  .card {
    position: absolute;
    left: 257px;
    top: 299px;
    width: 687px;
    height: 402px;
    background: var(--card-cream);
    overflow: hidden;
  }
  .card-photo {
    position: absolute;
    inset: 0;
    background:
      linear-gradient(180deg, rgba(242,235,221,0) 0%, rgba(214,201,174,0.55) 45%, var(--photo-ground) 100%),
      linear-gradient(90deg, var(--photo-mid) 0%, var(--photo-light) 40%, var(--photo-mid) 100%);
    opacity: 0.75;
  }
  .accent-band {
    position: absolute;
    left: 374px;
    top: 33px;
    width: 313px;
    height: 98px;
  }
  .brand-name {
    position: absolute;
    left: 36px;
    top: 34px;
    color: var(--brand-dark);
    font-weight: 900;
    line-height: 1;
  }
  .brand-name .brand-main {
    display: block;
    font-size: 64px;
    letter-spacing: 1px;
  }
  .brand-name .brand-sub {
    display: block;
    margin-top: 12px;
    margin-left: 6px;
    font-size: 33px;
    letter-spacing: 1.5px;
  }
  .services {
    position: absolute;
    left: 38px;
    top: 164px;
    margin: 0;
    padding: 0;
    list-style: none;
  }
  .services li {
    display: flex;
    align-items: center;
    height: 32px;
    font-size: 18px;
    font-weight: 700;
    color: var(--brand-dark);
  }
  .services .bullet {
    width: 18px;
    height: 18px;
    margin-right: 14px;
    background: var(--brand-brown);
  }
  .contact {
    position: absolute;
    margin: 0;
    font-size: 15px;
    line-height: 19px;
    color: var(--contact-brown);
    font-style: normal;
  }
  .contact-postal { left: 39px; top: 285px; }
  .contact-online { left: 374px; top: 322px; }
</style>
</head>
<body>
  <div class="card">
    <div class="card-photo" role="img" aria-label="Faded photograph of a single-storey house with white porch and front lawn"></div>

    <svg class="accent-band" viewBox="0 0 313 98" aria-hidden="true">
      <rect width="313" height="98" fill="var(--band-brown)"/>
      <g fill="var(--band-line)">
        <rect y="8" width="313" height="3"/>
        <rect y="23" width="313" height="3"/>
        <rect y="38" width="313" height="3"/>
        <rect y="53" width="313" height="3"/>
        <rect y="70" width="313" height="3"/>
        <rect y="86" width="313" height="3"/>
      </g>
    </svg>

    <div class="brand-name">
      <span class="brand-main">DUNLOW</span>
      <span class="brand-sub">CONSTRUCTION</span>
    </div>

    <ul class="services">
      <li><span class="bullet"></span>Class A Contractor</li>
      <li><span class="bullet"></span>NEW Home Construction &amp; Additions</li>
    </ul>

    <address class="contact contact-postal">
      Dunlow Construction, Inc<br>
      4827 E. Halbrim Dr.<br>
      Norfolk, VA 23999<br>
      555-214-3907
    </address>

    <address class="contact contact-online">
      DunlowConstruction@mailbrook.net<br>
      www.KTHouseMend.net
    </address>
  </div>
</body>
</html>
```